Help me improve my App on Human Shade Recall

Shade Recall Project. This altruistic project seeks to test and improve Shade Recall. According to ophthalmologists human eyes and brains can distinguish among a million colors. Now how do we communicate colors with each other. How do we test our mental capacity to recognize and remember colors? This App takes a step in this direction.

Help me improve this App - https://apps.brindleport.com/us/app/shade-recall-meter/id5829307746

```html
<!DOCTYPE html>
<html lang="en">
<head>
<meta charset="utf-8">
<title>Shade Recall – Home</title>
<link rel="stylesheet" href="https://fonts.googleapis.com/css2?family=Open+Sans:wght@400;600;700;800&display=swap">
<style>
  :root {
    --bg-light: #f8f7f3;
    --bg-mid: #ecebe6;
    --bg-dark: #dedcd5;
    --ink: #111111;
    --paper: #ffffff;
    --alert-red: #e0252b;
  }
  html, body {
    margin: 0;
    padding: 0;
    width: 1200px;
    height: 2598px;
    overflow: hidden;
  }
  .home-screen {
    position: relative;
    width: 1200px;
    height: 2598px;
    overflow: hidden;
    background: linear-gradient(160deg, var(--bg-mid) 0%, var(--bg-light) 35%, var(--bg-light) 55%, var(--bg-dark) 100%);
    font-family: "Open Sans", Arial, sans-serif;
    color: var(--ink);
  }
  .profile-button {
    position: absolute;
    left: 56px;
    top: 38px;
    width: 210px;
    height: 210px;
  }
  .player-slider {
    position: absolute;
    left: 30px;
    top: 272px;
    width: 266px;
    height: 50px;
  }
  .settings-button {
    position: absolute;
    left: 1004px;
    top: 36px;
    width: 156px;
    height: 156px;
  }
  .app-title {
    position: absolute;
    left: 0;
    top: 1118px;
    width: 1200px;
    margin: 0;
    text-align: center;
    font-size: 84px;
    font-weight: 600;
    letter-spacing: 0;
    line-height: 1;
  }
  .menu-grid {
    position: absolute;
    left: 100px;
    top: 1580px;
    width: 1000px;
    display: grid;
    grid-template-columns: repeat(3, 236px);
    column-gap: 132px;
    row-gap: 230px;
    justify-content: center;
  }
  .menu-item {
    width: 236px;
    height: 236px;
    display: block;
  }
  .menu-item svg { width: 100%; height: 100%; display: block; }
</style>
</head>
<body>
<main class="home-screen">

  <svg class="profile-button" viewBox="0 0 66 66" aria-label="Profile">
    <circle cx="33" cy="33" r="31" fill="none" stroke="var(--ink)" stroke-width="3.4"/>
    <circle cx="33" cy="26" r="10.5" fill="none" stroke="var(--ink)" stroke-width="3"/>
    <path d="M13 55 C15 44 22 40 33 40 C44 40 51 44 53 55" fill="none" stroke="var(--ink)" stroke-width="3"/>
  </svg>

  <svg class="player-slider" viewBox="0 0 84 16" aria-label="Players 1 to 2">
    <rect x="8" y="6" width="68" height="4" fill="none" stroke="var(--ink)" stroke-width="1.2"/>
    <circle cx="8" cy="8" r="6.4" fill="var(--paper)" stroke="var(--ink)" stroke-width="1.3"/>
    <circle cx="76" cy="8" r="6.4" fill="var(--paper)" stroke="var(--ink)" stroke-width="1.3"/>
    <text x="8" y="11" text-anchor="middle" font-size="8" font-weight="700" font-family="Open Sans, sans-serif" fill="var(--ink)">1</text>
    <text x="76" y="11" text-anchor="middle" font-size="8" font-weight="700" font-family="Open Sans, sans-serif" fill="var(--ink)">2</text>
  </svg>

  <svg class="settings-button" viewBox="0 0 50 50" aria-label="Settings">
    <g fill="var(--ink)">
      <rect x="1" y="8" width="48" height="5" rx="2.5"/>
      <rect x="1" y="22.5" width="48" height="5" rx="2.5"/>
      <rect x="1" y="37" width="48" height="5" rx="2.5"/>
      <circle cx="34" cy="10.5" r="6"/>
      <circle cx="38" cy="25" r="6"/>
      <circle cx="15" cy="39.5" r="6"/>
    </g>
  </svg>

  <h1 class="app-title">Shade Recall</h1>

  <nav class="menu-grid">
    <a class="menu-item exam-button" aria-label="Exam">
      <svg viewBox="0 0 74 74">
        <path d="M27 7 h20 v5 h5 v6 h-30 v-6 h5z" fill="var(--paper)" stroke="var(--ink)" stroke-width="3" stroke-linejoin="round"/>
        <rect x="9" y="12" width="56" height="58" rx="3" fill="var(--paper)" stroke="var(--ink)" stroke-width="3.2"/>
        <text x="37" y="35" text-anchor="middle" font-size="13" font-weight="800" font-family="Open Sans, sans-serif" fill="var(--ink)">EXAM</text>
        <path d="M15 45 l3 3 l6 -6" fill="none" stroke="var(--ink)" stroke-width="2.6"/>
        <path d="M15 54 l7 7 M22 54 l-7 7" stroke="var(--ink)" stroke-width="2.6"/>
        <rect x="30" y="45" width="26" height="3" fill="var(--ink)"/>
        <rect x="30" y="56" width="26" height="3" fill="var(--ink)"/>
      </svg>
    </a>

    <a class="menu-item train-button" aria-label="Vision training">
      <svg viewBox="0 0 74 74">
        <path d="M4 48 C16 30 58 30 70 48 C58 66 16 66 4 48 Z" fill="var(--ink)"/>
        <path d="M12 48 C22 37 52 37 62 48 C52 59 22 59 12 48 Z" fill="var(--paper)"/>
        <circle cx="37" cy="48" r="10" fill="var(--ink)"/>
        <circle cx="33" cy="45" r="3" fill="var(--paper)"/>
        <path d="M37 40 V14" stroke="var(--ink)" stroke-width="3"/>
        <path d="M37 3 L30 18 L44 18 Z" fill="var(--paper)" stroke="var(--ink)" stroke-width="2.4" stroke-linejoin="round"/>
      </svg>
    </a>

    <a class="menu-item daily-button" aria-label="24 hour challenge">
      <svg viewBox="0 0 74 74">
        <circle cx="38" cy="38" r="31" fill="var(--paper)" stroke="var(--ink)" stroke-width="3"/>
        <g stroke="var(--ink)" stroke-width="3">
          <path d="M38 7 v6 M38 63 v6 M7 38 h6 M63 38 h6"/>
          <path d="M60 16 l-4 4 M16 60 l4 -4 M60 60 l-4 -4"/>
        </g>
        <text x="39" y="41" text-anchor="middle" font-size="19" font-weight="800" font-family="Open Sans, sans-serif" fill="var(--alert-red)">24</text>
        <text x="39" y="53" text-anchor="middle" font-size="10" font-weight="800" font-family="Open Sans, sans-serif" fill="var(--ink)">HRS</text>
        <circle cx="13" cy="13" r="8" fill="var(--alert-red)"/>
      </svg>
    </a>

    <a class="menu-item info-button" aria-label="Information">
      <svg viewBox="0 0 74 74">
        <rect x="10" y="4" width="56" height="60" rx="4" fill="var(--ink)"/>
        <path d="M10 60 C10 56 13 54 17 54 H66 V70 H17 C13 70 10 68 10 64 Z" fill="var(--ink)"/>
        <rect x="16" y="58" width="50" height="7" fill="var(--paper)"/>
        <circle cx="38" cy="28" r="15" fill="var(--paper)"/>
        <circle cx="38" cy="20" r="2.6" fill="var(--ink)"/>
        <rect x="35.5" y="25" width="5" height="13" fill="var(--ink)"/>
      </svg>
    </a>

    <a class="menu-item versus-button" aria-label="Versus mode">
      <svg viewBox="0 0 74 74">
        <circle cx="37" cy="37" r="27" fill="var(--paper)" stroke="var(--ink)" stroke-width="6"/>
        <path d="M6 68 L68 6" stroke="var(--ink)" stroke-width="6" stroke-linecap="round"/>
        <text x="37" y="45" text-anchor="middle" font-size="22" font-weight="800" font-family="Open Sans, sans-serif" fill="var(--ink)">VS</text>
      </svg>
    </a>

    <a class="menu-item ranking-button" aria-label="Leaderboard">
      <svg viewBox="0 0 74 74">
        <rect x="4" y="48" width="22" height="22" fill="var(--ink)"/>
        <rect x="26" y="40" width="22" height="30" fill="var(--ink)" stroke="var(--paper)" stroke-width="1"/>
        <rect x="48" y="52" width="22" height="18" fill="var(--ink)"/>
        <text x="15" y="66" text-anchor="middle" font-size="13" font-weight="800" font-family="Open Sans, sans-serif" fill="var(--paper)">2</text>
        <text x="37" y="60" text-anchor="middle" font-size="13" font-weight="800" font-family="Open Sans, sans-serif" fill="var(--paper)">1</text>
        <text x="59" y="67" text-anchor="middle" font-size="13" font-weight="800" font-family="Open Sans, sans-serif" fill="var(--paper)">3</text>
      </svg>
    </a>
  </nav>

</main>
</body>
</html>
```